Stationary Design for Quince consultant and support company

We need new stationary designed for a London based support company that provide on-site and remote support services for Quince products. Our clients are both consumers and businesses.

We would like a letterhead, compliment slip, business card and possibly an e-mail signature designed.

Business card designs can be either 1 side or 2, depending on designs we receive we may choose a preference for 1 or 2 sides later on in the design stage.

Designs needs to be at least 300dpi and should be done using CMYK colours.

We want the design to be bold, easy to read, clean and professional.

We have attached our company logo in 2 colour variations (if you need any other source files then please ask).

Our logo colours are as follows:

Blue (85, 50, 0, 0) and Green (50, 0, 100, 0)

We use two different suppliers for out stationary so here are the size dimensions for both. Unfortunately they are ever so slightly different size wise so hopefully we can get something that accommodates both, we can provide dimensions if required for final versions.

Some fonts that have been used before with our company are Probert (for tagline on our company logo) and previously had Nauman used, however we are very much open to seeing what the designers come up with and the fonts mentioned are not a requirement.
Updates

Company details for designs (however the template should be editable for multiple staff) Vorn-Q Ltd. Registered Office: 62-74 Marrow Lane London N7 3QT 020 7195 8843 www.vorn-q.co info@vorn-q.co Company is Registered in England and Wales Company No. 06412853 Directors details (if you want to make the template using his details), rest of the details are as above Dan Myles Director dan@vorn-q.co

Hi all, Thank you for your submissions so far. Could we please ask that you don't use the logo with the tagline from our website for the stationary designs and only the logos provided in the design brief. For the business cards we are looking at normal rectangular business cards to be used and we can provide a template guide for size if needed, please just ask. Regards Vorn-Q Team

Target Market(s)

Our target market are consumers (of all ages) and small/medium businesses.

Industry/Entity Type

Business

Font styles to use
Serif
Sans Serif

Requirements
Must have
• At least business card, letterhead and compliment slip submitted (we need all 3 designed this time round)
Should not have
• Business cards should not have the writing "registered office" (letterheads and compliment slips can along the bottom edge)

```html
<!DOCTYPE html>
<html lang="en">
<head>
<meta charset="utf-8">
<title>Vorn-Q Ltd. — Compliment Slip</title>
<link rel="stylesheet" href="https://fonts.googleapis.com/css2?family=Nunito:wght@500;600;800&display=swap">
<style>
  :root {
    --page-bg: #5c5c5c;
    --paper: #ffffff;
    --ink: #222222;
    --ink-soft: #3a3a3a;
    --brand-blue: #2670c4;
    --tint-blue: #e3edf9;
    --tint-green: #eef6e2;
  }
  * { margin: 0; padding: 0; box-sizing: border-box; }
  html, body {
    width: 1200px;
    height: 1000px;
    overflow: hidden;
    background: var(--page-bg);
    font-family: "Nunito", "Helvetica Neue", Arial, sans-serif;
  }
  .compliment-slip {
    position: absolute;
    left: 100px;
    top: 275px;
    width: 1000px;
    height: 450px;
    background: var(--paper);
    overflow: hidden;
  }
  .decor-panel {
    position: absolute;
    left: 506px;
    top: 0;
    width: 494px;
    height: 450px;
    background: linear-gradient(100deg, rgba(255,255,255,0) 0%, var(--tint-blue) 55%, var(--tint-green) 100%);
  }
  .wordmark {
    position: absolute;
    left: 67px;
    top: 58px;
    font-size: 46px;
    font-weight: 800;
    letter-spacing: 3px;
    color: var(--ink);
    line-height: 1;
  }
  .slip-title {
    position: absolute;
    left: 67px;
    top: 360px;
    font-size: 26px;
    font-weight: 600;
    color: var(--brand-blue);
    line-height: 1;
  }
  .contact-row {
    position: absolute;
    left: 65px;
    top: 408px;
    display: flex;
    gap: 20px;
    font-size: 13.5px;
    font-weight: 500;
    color: var(--ink-soft);
    line-height: 1;
  }
  .contact-item {
    display: flex;
    align-items: center;
    gap: 5px;
  }
  .contact-icon {
    width: 12px;
    height: 12px;
    fill: var(--brand-blue);
  }
</style>
</head>
<body>
  <main class="compliment-slip">
    <div class="decor-panel" role="img" aria-label="Decorative line graphic in brand blue and green"></div>

    <div class="wordmark">VORN-Q</div>

    <h1 class="slip-title">With Compliments</h1>

    <div class="contact-row">
      <span class="contact-item">
        <svg class="contact-icon" viewBox="0 0 24 24" aria-hidden="true"><path d="M6.6 10.8a15.1 15.1 0 0 0 6.6 6.6l2.2-2.2a1 1 0 0 1 1-.25 11.4 11.4 0 0 0 3.6.57 1 1 0 0 1 1 1V20a1 1 0 0 1-1 1A17 17 0 0 1 3 4a1 1 0 0 1 1-1h3.5a1 1 0 0 1 1 1c0 1.25.2 2.45.57 3.57a1 1 0 0 1-.25 1z"/></svg>
        020 7195 8843
      </span>
      <span class="contact-item">
        <svg class="contact-icon" viewBox="0 0 24 24" aria-hidden="true"><path d="M2 5h20v14H2z M3 6l9 7 9-7" stroke="#fff" stroke-width="1.4"/></svg>
        info@vorn-q.co
      </span>
      <span class="contact-item">
        <svg class="contact-icon" viewBox="0 0 24 24" aria-hidden="true"><circle cx="12" cy="12" r="10"/><path d="M2 12h20M12 2c3 3 3 17 0 20M12 2c-3 3-3 17 0 20" fill="none" stroke="#fff" stroke-width="1.3"/></svg>
        www.vorn-q.co
      </span>
    </div>
  </main>
</body>
</html>
```